Business cards and stationary
Maple Hollow Real Estate Investments
Simple
Teresa Vilk
Owner
4817 Lindell Ct
Larkfield, CO 80999
maplehollowrei@quillmail.example
We specialize in buying, renovating, reselling and renting homes and muti-unit properties in the Denver area
Logo
Vector logo

```html
<!DOCTYPE html>
<html lang="en">
<head>
<meta charset="utf-8">
<title>Maple Hollow Real Estate Investments – Stationery</title>
<link href="https://fonts.googleapis.com/css2?family=Open+Sans:wght@400;600;700&display=swap" rel="stylesheet">
<style>
  :root {
    --backdrop: #b9babc;
    --paper: #ffffff;
    --brand-red: #c5281f;
    --ink: #1d1d1d;
    --rule: #b5b5b5;
    --window: #d3d4d6;
    --faint-house: #f6d8cd;
    --band-text: #f6e3e1;
  }
  * { box-sizing: border-box; margin: 0; padding: 0; }
  html, body { width: 1200px; height: 859px; overflow: hidden; }
  body {
    background: var(--backdrop);
    font-family: "Open Sans", Arial, sans-serif;
    color: var(--ink);
    position: relative;
  }
  .sheet { position: absolute; background: var(--paper); overflow: hidden; }

  .brand { position: absolute; display: flex; flex-direction: column; }
  .brand-row { display: flex; align-items: center; gap: 6px; }
  .brand-mark { background: var(--brand-red); flex: none; }
  .brand-name { font-weight: 700; color: var(--brand-red); line-height: 1; white-space: nowrap; }
  .brand-tag { font-weight: 700; color: var(--ink); letter-spacing: 0.12em; white-space: nowrap; text-transform: uppercase; }

  .red-band {
    position: absolute; left: 0; right: 0; bottom: 0;
    background: var(--brand-red);
    border-top: 3px solid var(--ink);
    color: var(--band-text);
    display: flex; align-items: center;
  }
  .house-mark { position: absolute; background: var(--faint-house); opacity: .8; }

  /* business card front */
  .card-front { left: 211px; top: 60px; width: 228px; height: 149px; }
  .card-front .brand { left: 22px; top: 12px; }
  .card-front .brand-mark { width: 19px; height: 19px; }
  .card-front .brand-name { font-size: 19px; }
  .card-front .brand-tag { font-size: 5px; margin-left: 25px; margin-top: 1px; }
  .card-person { position: absolute; left: 0; right: 0; top: 68px; text-align: center; }
  .card-name { font-size: 7px; font-weight: 700; color: var(--ink); }
  .card-title { font-size: 6px; color: var(--brand-red); }
  .card-front .red-band { height: 38px; font-size: 4.5px; justify-content: space-between; padding: 0 16px; }
  .card-contact { display: flex; flex-direction: column; gap: 3px; }

  /* business card back */
  .card-back { left: 211px; top: 233px; width: 228px; height: 144px; }

  /* letterhead */
  .letterhead { left: 612px; top: 43px; width: 564px; height: 756px; }
  .letterhead .brand { left: 35px; top: 22px; }
  .letterhead .brand-mark { width: 26px; height: 26px; }
  .letterhead .brand-name { font-size: 27px; }
  .letterhead .brand-tag { font-size: 6.5px; margin-left: 32px; margin-top: 2px; }
  .head-rule { position: absolute; left: 255px; right: 24px; top: 70px; height: 1px; background: var(--rule); }
  .letterhead .house-mark { right: 0; bottom: 38px; width: 168px; height: 118px; }
  .letterhead .red-band { height: 38px; font-size: 5.5px; justify-content: center; gap: 18px; }

  /* envelope */
  .envelope { left: 29px; top: 415px; width: 564px; height: 384px; background: transparent; }
  .envelope svg.flap { position: absolute; left: 0; top: 0; }
  .envelope .brand { left: 48px; top: 142px; }
  .envelope .brand-mark { width: 28px; height: 28px; }
  .envelope .brand-name { font-size: 28px; }
  .envelope .brand-tag { font-size: 7px; margin-left: 34px; margin-top: 2px; }
  .env-window { position: absolute; left: 50px; top: 233px; width: 274px; height: 84px; background: var(--window); border: 1px solid #a9aaac; border-radius: 8px; }
  .envelope .house-mark { left: 415px; top: 228px; width: 149px; height: 115px; }
  .envelope .red-band { height: 38px; font-size: 5.5px; justify-content: center; }
</style>
</head>
<body>

  <section class="sheet card-front">
    <div class="brand">
      <div class="brand-row"><span class="brand-mark"></span><span class="brand-name">MapleHollow</span></div>
      <span class="brand-tag">Real Estate Investments</span>
    </div>
    <div class="card-person">
      <p class="card-name">Teresa Vilk</p>
      <p class="card-title">Owner</p>
    </div>
    <div class="red-band">
      <span>4817 Lindell Ct · Larkfield, CO 80999</span>
      <div class="card-contact">
        <span>P: 303-555-0147</span>
        <span>E: maplehollowrei@quillmail.example</span>
      </div>
    </div>
  </section>

  <section class="sheet card-back"></section>

  <section class="sheet envelope">
    <svg class="flap" width="564" height="384" viewBox="0 0 564 384">
      <path d="M0 44 L280 0 L564 44 L564 384 L0 384 Z" fill="#ffffff"/>
      <path d="M0 44 L280 0 L564 44" fill="none" stroke="#8d8e90" stroke-width="1"/>
      <path d="M0 44 L280 96 L564 44" fill="none" stroke="#d6d6d6" stroke-width="1"/>
    </svg>
    <div class="brand">
      <div class="brand-row"><span class="brand-mark"></span><span class="brand-name">MapleHollow</span></div>
      <span class="brand-tag">Real Estate Investments</span>
    </div>
    <div class="env-window"></div>
    <div class="house-mark" role="img" aria-label="Faint house emblem decoration"></div>
    <div class="red-band"><span>4817 Lindell Ct · Larkfield, CO 80999</span></div>
  </section>

  <section class="sheet letterhead">
    <div class="brand">
      <div class="brand-row"><span class="brand-mark"></span><span class="brand-name">MapleHollow</span></div>
      <span class="brand-tag">Real Estate Investments</span>
    </div>
    <div class="head-rule"></div>
    <div class="house-mark" role="img" aria-label="Faint house emblem decoration"></div>
    <div class="red-band">
      <span>4817 Lindell Ct · Larkfield, CO 80999</span>
      <span>P: 303-555-0147</span>
      <span>E: maplehollowrei@quillmail.example</span>
    </div>
  </section>

</body>
</html>
```